KVR Inc Web Design

WHAT ARE WE DOING?
We are developing a new website look and feel for a new company called KVR Inc. This new look and feel should include colors, design elements, choice of photography and other imagery, fonts, and other user experience elements.

WHAT DO THEY DO?
KVR, Inc, makes tools for researchers who are studying protein-protein interactions. These molecules are the basic tools of biology, and serve as key targets for drug developers and disease researchers. The world of proteins is enormously complex, and companies like KVR provide researchers with critical tools that help them elucidate this world.

WHO ARE WE TALKING TO?
The target audience for this website are professional scientists working in university research or biopharma drug development. They are highly sophisticated consumers looking for key tools that will advance their research.

WHAT DO WE WANT THEM TO DO?
The site is an information resource for the customer exploring the tools that KVR sells and the scientific issues surrounding protein-protein interactions. They should be able to navigate easily to their content of choice, while the whole site should convey a professionalism that enhanced KVR’s credibility.

WHAT DOES THE KVR BRAND STAND FOR?
KVR stands for illumination. Proteins are challenging to study, and KVR exists to help shed light on their workings.

WHAT ARE THE KEY VALUES OF THE KVR BRAND?
Integrity. Innovation. Insight.

WHAT ARE THE EXECUTIONAL MANDITORIES?
The look and feel is completely up for grabs. Nothing is off the table.

WHAT ARE THE DELIVERABLES?
We need new designs for the following templates:
http://cms.orvadeltaworks.com/
http://cms.orvadeltaworks.com/products-and-services/instruments-3/bench-top-instruments/
http://cms.orvadeltaworks.com/category/lab-study/

```html
<!DOCTYPE html>
<html lang="en">
<head>
<meta charset="utf-8">
<title>KVR Inc</title>
<link rel="stylesheet" href="https://fonts.googleapis.com/css2?family=Source+Sans+3:wght@300;400;600&display=swap">
<style>
  :root {
    --orange-top: #ffc060;
    --orange-bottom: #f7941d;
    --orange-line: #e08410;
    --nav-text: #5a3500;
    --ink: #3a3a3a;
    --muted: #555;
    --band: #ececec;
    --footer: #414141;
    --footer-rule: #e2e2e2;
    --white: #ffffff;
  }
  * { margin: 0; padding: 0; box-sizing: border-box; }
  html, body { width: 1200px; height: 1074px; overflow: hidden; background: var(--white); }
  body { position: relative; font-family: "Source Sans 3", sans-serif; color: var(--ink); }
  .top-strip { position: absolute; left: 0; top: 0; width: 1200px; height: 6px; background: #e6e6e6; }
  .brand { position: absolute; left: 89px; top: 34px; width: 227px; height: 51px; background: #f6f6f6;
    display: flex; align-items: center; justify-content: center; font-size: 42px; font-weight: 400;
    letter-spacing: 8px; color: #555; }
  .search { position: absolute; left: 839px; top: 56px; width: 248px; height: 31px; border: 1px solid #d4d4d4; display: flex; }
  .search-field { flex: 1; padding-left: 12px; line-height: 29px; font-size: 13px; font-style: italic; color: #888; font-weight: 300; }
  .search-btn { width: 32px; border-left: 1px solid #d4d4d4; background: #f4f4f4; display: flex; align-items: center; justify-content: center; }
  .main-nav { position: absolute; left: 110px; top: 108px; width: 980px; height: 48px; display: flex;
    background: linear-gradient(var(--orange-top), var(--orange-bottom)); border: 1px solid var(--orange-line); }
  .main-nav a { display: flex; align-items: center; justify-content: center; font-size: 19px; color: var(--nav-text);
    text-decoration: none; border-right: 1px solid var(--orange-line); }
  .main-nav a:last-child { border-right: none; }
  .hero-band { position: absolute; left: 0; top: 153px; width: 1200px; height: 407px; background: var(--band); }
  .hero { position: absolute; left: 110px; top: 156px; width: 980px; height: 404px;
    background: linear-gradient(100deg, #cfdbe6 0%, #eef2f6 40%, #f7f4f0 65%, #d9e3ee 100%); }
  .hero-caption { position: absolute; left: 151px; top: 357px; width: 408px; height: 155px; background: rgba(70,70,72,.88); color: var(--white); padding: 20px 30px; }
  .hero-caption h1 { font-size: 32px; font-weight: 300; line-height: 36px; }
  .hero-caption h2 { font-size: 24px; font-weight: 300; line-height: 28px; }
  .hero-caption p { font-size: 13px; font-weight: 300; line-height: 19px; color: #cfcfcf; margin-top: 6px; }
  .hero-toggle { position: absolute; left: 1050px; top: 525px; width: 40px; height: 35px; background: #4a4a4a; display: flex; align-items: center; justify-content: center; }
  .feature { position: absolute; top: 604px; width: 306px; }
  .feature-photo { width: 306px; height: 133px; }
  .feature h3 { font-size: 26px; font-weight: 300; margin-top: 8px; line-height: 32px; color: #333; }
  .feature p { font-size: 14px; font-weight: 300; line-height: 19px; color: var(--muted); margin-top: 5px; }
  .btn { display: inline-block; margin-top: 12px; width: 100px; height: 27px; line-height: 25px; text-align: center; font-size: 12px;
    color: var(--nav-text); background: linear-gradient(var(--orange-top), var(--orange-bottom)); border: 1px solid var(--orange-line); border-radius: 2px; }
  .footer-rule { position: absolute; left: 0; top: 957px; width: 1200px; height: 8px; background: var(--footer-rule); }
  .site-footer { position: absolute; left: 0; top: 965px; width: 1200px; height: 109px; background: var(--footer); }
  .footer-links { position: absolute; left: 113px; top: 25px; font-size: 15px; color: var(--white); }
  .footer-links span { margin: 0 5px; }
  .copyright { position: absolute; left: 113px; top: 56px; font-size: 12px; color: #b8b8b8; font-weight: 300; }
  .social { position: absolute; left: 967px; top: 23px; display: flex; gap: 3px; }
  .social span { width: 30px; height: 30px; border-radius: 50%; background: var(--white); }
</style>
</head>
<body>
  <div class="top-strip"></div>
  <div class="brand">KVR INC</div>
  <div class="search">
    <div class="search-field">Search here..</div>
    <div class="search-btn">
      <svg width="16" height="16" viewBox="0 0 16 16"><circle cx="7" cy="7" r="5" fill="none" stroke="#777" stroke-width="2"/><line x1="11" y1="11" x2="15" y2="15" stroke="#777" stroke-width="2.5"/></svg>
    </div>
  </div>
  <nav class="main-nav">
    <a style="width:166px">Company</a>
    <a style="width:200px">Product &amp; Services</a>
    <a style="width:184px">Learning Center</a>
    <a style="width:121px">Events</a>
    <a style="width:138px">KVR News</a>
    <a style="width:169px">Contact Us</a>
  </nav>
  <div class="hero-band"></div>
  <div class="hero" role="img" aria-label="Smiling scientist in a lab coat in a bright laboratory"></div>
  <div class="hero-caption">
    <h1>Mauris vel lacus vitae felis</h1>
    <h2>Vivamus sollicitudin metus</h2>
    <p>Mauris vel lacus vitae felis vestibulum volutpat. Etiam est nunc, venenatis in, tristique eu, imperdiet ac, nisl.</p>
  </div>
  <div class="hero-toggle">
    <svg width="24" height="16" viewBox="0 0 24 16"><polyline points="8,2 2,8 8,14" fill="none" stroke="#fff" stroke-width="1.6"/><polyline points="16,2 22,8 16,14" fill="none" stroke="#fff" stroke-width="1.6"/></svg>
  </div>

  <section class="feature" style="left:110px">
    <div class="feature-photo" role="img" aria-label="Researcher in mask and goggles examining a test tube" style="background:linear-gradient(90deg,#d8dde0,#9fb6bf 60%,#e4e8ea)"></div>
    <h3>Innovation</h3>
    <p>Lorem ipsum dolor sit amet, consectetur adipiscing elit. Proin placerat nulla massa, a condimentum leo tincidunt vel. Consectetur adipiscing elit. Proin placerat nulla massa, a condimentum leo.</p>
    <span class="btn">LEARN MORE</span>
  </section>
  <section class="feature" style="left:447px">
    <div class="feature-photo" role="img" aria-label="Automated lab equipment holding sample vials" style="background:linear-gradient(120deg,#5c6fb0,#a9b6df 50%,#dfe5f3)"></div>
    <h3>Automation</h3>
    <p>Lorem ipsum dolor sit amet, consectetur adipiscing elit. Proin placerat nulla massa, a condimentum leo tincidunt vel. Consectetur adipiscing elit. Proin placerat nulla massa, a condimentum leo.</p>
    <span class="btn">ORDER NOW</span>
  </section>
  <section class="feature" style="left:784px">
    <div class="feature-photo" role="img" aria-label="Scientist at a microscope beside a molecule model on screen" style="background:linear-gradient(90deg,#3a4048,#b9c9d8 45%,#eef2f5)"></div>
    <h3>Research</h3>
    <p>Lorem ipsum dolor sit amet, consectetur adipiscing elit. Proin placerat nulla massa, a condimentum leo tincidunt vel. Consectetur adipiscing elit. Proin placerat nulla massa, a condimentum leo.</p>
    <span class="btn">THE CHALLENGE</span>
  </section>

  <div class="footer-rule"></div>
  <footer class="site-footer">
    <div class="footer-links">Home<span>|</span>Company<span>|</span>Products &amp; Services<span>|</span>Contact Us<span>|</span>Site Map</div>
    <div class="copyright">© 2013 Company Name.&nbsp; All right reserved</div>
    <div class="social" aria-label="Social links"><span></span><span></span><span></span><span></span></div>
  </footer>
</body>
</html>
```